Plumwave business card

We need a modern business card - With our 4 colors - See web: www.plumwave.dk

I have attached logo and som old business Cards we have - Lets Make the new ones shine...:-) -

Industry/Entity Type

Business

Requirements
Must have
• the logo with plumwave only,

```html
<!DOCTYPE html>
<html lang="da">
<head>
<meta charset="utf-8">
<title>Plumwave business card</title>
<link rel="stylesheet" href="https://fonts.googleapis.com/css2?family=Josefin+Sans:wght@400;600&display=swap">
<style>
  :root {
    --backdrop: #e9e6e1;
    --card: #3c3c3e;
    --pink: #c7338c;
    --lime: #8cc63f;
    --orange: #e8842b;
    --purple: #6d2a7e;
    --ink: #3c3c3e;
  }
  * { box-sizing: border-box; margin: 0; padding: 0; }
  html, body { width: 1200px; height: 1023px; overflow: hidden; }
  body {
    background: var(--backdrop);
    font-family: "Josefin Sans", Arial, sans-serif;
    position: relative;
  }
  .card {
    position: absolute;
    width: 720px; height: 440px;
    background: var(--card);
    border-radius: 4px;
    box-shadow: 0 14px 32px rgba(0,0,0,.25);
    overflow: hidden;
  }
  .card-front { left: 240px; top: 45px; }
  .card-back { left: 240px; top: 538px; }

  /* front */
  .identity {
    position: absolute;
    left: 44px; top: 122px;
    width: 290px;
    text-align: center;
  }
  .brand {
    display: flex; align-items: center; justify-content: center; gap: 12px;
    color: var(--lime);
    font-size: 32px; font-weight: 600;
    margin-bottom: 30px;
  }
  .brand-dot {
    width: 21px; height: 21px; border-radius: 50%;
    background: var(--lime);
  }
  .person-name {
    color: var(--orange);
    font-size: 29px;
    padding-bottom: 6px;
    border-bottom: 3px solid var(--lime);
  }
  .person-role { color: var(--orange); font-size: 28px; margin-top: 10px; }
  .person-title { color: var(--pink); font-size: 23px; margin-top: 4px; }

  .timeline { position: absolute; left: 383px; top: 0; width: 5px; height: 440px; }
  .seg { position: absolute; left: 0; width: 5px; }
  .seg-pink { top: 0; height: 130px; background: var(--pink); }
  .seg-lime { top: 130px; height: 107px; background: var(--lime); }
  .seg-orange { top: 237px; height: 139px; background: var(--orange); }
  .seg-purple { top: 376px; height: 64px; background: var(--purple); }

  .icon {
    position: absolute; left: 362px;
    width: 46px; height: 46px; border-radius: 50%;
    display: flex; align-items: center; justify-content: center;
  }
  .icon svg { width: 23px; height: 23px; }
  .icon-pin { top: 101px; background: var(--pink); }
  .icon-phone { top: 199px; background: var(--lime); }
  .icon-mail { top: 298px; background: var(--orange); }

  .contact {
    position: absolute; left: 434px;
    color: var(--lime);
    font-size: 21px; line-height: 31px;
    letter-spacing: .4px;
  }
  .contact-address { top: 93px; }
  .contact-phone { top: 191px; }
  .contact-mail { top: 290px; }

  /* back */
  .block { position: absolute; width: 96px; height: 48px; }
  .block-purple { left: 0; top: 0; background: var(--purple); }
  .block-green { left: 96px; top: 0; background: var(--lime); }
  .block-orange { right: 96px; bottom: 0; background: var(--orange); }
  .block-pink { right: 0; bottom: 0; background: var(--pink); }
</style>
</head>
<body>
  <section class="card card-front" aria-label="Plumwave business card, front">
    <div class="identity">
      <div class="brand"><span class="brand-dot"></span>Plumwave</div>
      <div class="person-name">Jonas Vesterby</div>
      <div class="person-role">CEO</div>
      <div class="person-title">Salgsdirector</div>
    </div>

    <div class="timeline">
      <span class="seg seg-pink"></span>
      <span class="seg seg-lime"></span>
      <span class="seg seg-orange"></span>
      <span class="seg seg-purple"></span>
    </div>

    <div class="icon icon-pin">
      <svg viewBox="0 0 24 24"><path d="M3 5 L21 5 L12 21 Z" fill="var(--ink)"/><circle cx="12" cy="10" r="3" fill="var(--pink)"/></svg>
    </div>
    <div class="icon icon-phone">
      <svg viewBox="0 0 24 24"><path d="M2 9 Q12 1 22 9 L19 12 L16 10 L16 8 Q12 6 8 8 L8 10 L5 12 Z" fill="var(--ink)"/><rect x="6" y="13" width="12" height="8" rx="2" fill="var(--ink)"/><circle cx="12" cy="17" r="2" fill="var(--lime)"/></svg>
    </div>
    <div class="icon icon-mail">
      <svg viewBox="0 0 24 24"><rect x="2" y="5" width="20" height="14" rx="1" fill="var(--ink)"/><path d="M2 5 L12 13 L22 5" fill="none" stroke="var(--orange)" stroke-width="2"/></svg>
    </div>

    <p class="contact contact-address">Lindevej 14<br>2000 Frederiksberg</p>
    <p class="contact contact-phone">+45 31 20 40 60<br>+45 52 60 70 80</p>
    <p class="contact contact-mail">jv@plumwave.dk<br>info@plumwave.dk</p>
  </section>

  <section class="card card-back" aria-label="Plumwave business card, back">
    <span class="block block-purple"></span>
    <span class="block block-green"></span>
    <span class="block block-orange"></span>
    <span class="block block-pink"></span>
  </section>
</body>
</html>
```